Card back (63 x 88 mm) design for new "Ember Tidefall" Collectible Trading Card Game

We are looking for something that has a beautiful, stunning, fantasy world feel, but dont forget that this is a card back side. Fonts similar to MagicMedieval and Runes of Vellmoor ("Ember Tidefall" Collectible Trading Card Game). This font will be used later in the front design also. It should be professional, beautiful, refreshing and stunning to look at.
Please feel free to use your imagination, maybe even using fantasy world elements. Feel free to google, "Qel card back images". We like the style of the black border like you see in the searched images.
We need this in 3 versions. Sizes: like in uploaded pdf will used in the digital version, for the printing house with an additional 5mm extra oversized (every side) and smaller as a picture for a PX Profile Picture.
We want something that is beautiful and inspiring and we can't wait to see what you work on!
Reason: We hope to get more designs
Target Market(s)
Worldwide
Font styles to use
Other font styles liked:
- MagicMedieval, Runes of Vellmoor
Requirements
Must have
- Design must look professional and well integrated.

```html
<!DOCTYPE html>
<html lang="en">
<head>
<meta charset="utf-8">
<title>Ember Tidefall – Card Back</title>
<link rel="stylesheet" href="https://fonts.googleapis.com/css2?family=Almendra+SC&display=swap">
<style>
  :root {
    --page-bg: #3a332d;
    --card-black: #0b0a0c;
    --edge-purple: #6e2a80;
    --edge-purple-glow: #b04fc4;
    --wood-dark: #24190f;
    --wood-mid: #45331f;
    --wood-light: #5a4430;
    --ember-gold: #e8a23a;
    --ember-hot: #f2c26a;
    --ember-red: #c2501c;
    --banner-bg: #2a0f33;
    --banner-border: #8a3fa0;
    --banner-text: #e9d6f0;
  }
  * { box-sizing: border-box; margin: 0; padding: 0; }
  html, body {
    width: 1200px;
    height: 800px;
    overflow: hidden;
    background: var(--page-bg);
  }
  .canvas {
    position: relative;
    width: 1200px;
    height: 800px;
  }
  .card-back {
    position: absolute;
    left: 356px;
    top: 60px;
    width: 487px;
    height: 680px;
    border-radius: 26px;
    background: var(--card-black);
    box-shadow: 0 10px 30px rgba(0, 0, 0, 0.45);
  }
  .card-back__frame {
    position: absolute;
    inset: 18px;
    border-radius: 8px;
    background: linear-gradient(180deg, var(--edge-purple), #4a1a58 50%, var(--edge-purple));
    box-shadow: 0 0 14px 2px rgba(176, 79, 196, 0.45);
  }
  .card-back__wood {
    position: absolute;
    inset: 8px;
    border-radius: 4px;
    overflow: hidden;
    background:
      repeating-linear-gradient(88deg, rgba(0,0,0,0.12) 0 3px, transparent 3px 14px, rgba(255,255,255,0.03) 14px 16px, transparent 16px 31px),
      linear-gradient(100deg, var(--wood-dark) 0%, var(--wood-mid) 30%, var(--wood-light) 55%, var(--wood-mid) 80%, var(--wood-dark) 100%);
    box-shadow: inset 0 0 46px 14px rgba(0, 0, 0, 0.7);
  }
  .card-back__ember-glow {
    position: absolute;
    left: 50%;
    top: 40px;
    width: 380px;
    height: 300px;
    transform: translateX(-50%);
    border-radius: 50%;
    background: radial-gradient(ellipse at 50% 50%,
      rgba(242, 194, 106, 0.38) 0%,
      rgba(232, 120, 40, 0.26) 35%,
      rgba(194, 80, 28, 0.10) 60%,
      transparent 72%);
  }
  .card-back__seal {
    position: absolute;
    left: 50%;
    top: 78px;
    width: 54px;
    height: 54px;
    transform: translateX(-50%);
    border-radius: 50%;
    background: var(--ember-gold);
  }
  .card-back__title {
    position: absolute;
    left: 0;
    right: 0;
    top: 150px;
    text-align: center;
    font-family: "Almendra SC", serif;
    font-weight: 400;
    font-size: 66px;
    line-height: 0.95;
    color: var(--ember-gold);
  }
  .card-back__banner {
    position: absolute;
    left: 50%;
    top: 448px;
    transform: translateX(-50%);
    white-space: nowrap;
    padding: 5px 16px 6px;
    background: var(--banner-bg);
    border: 2px solid var(--banner-border);
    border-radius: 2px;
    font-family: "Almendra SC", serif;
    font-size: 18px;
    letter-spacing: 0.5px;
    color: var(--banner-text);
  }
</style>
</head>
<body>
  <main class="canvas">
    <article class="card-back">
      <div class="card-back__frame" role="img" aria-label="Ragged purple glowing border framing the card">
        <div class="card-back__wood" role="img" aria-label="Dark weathered wood grain texture">
          <div class="card-back__ember-glow" role="img" aria-label="Fiery ember glow with drifting sparks behind the game title"></div>
          <span class="card-back__seal" aria-hidden="true"></span>
          <h1 class="card-back__title">Ember<br>Tidefall</h1>
          <p class="card-back__banner">Collectible Trading Card Game</p>
        </div>
      </div>
    </article>
  </main>
</body>
</html>
```